New Website for ReBranded Company - CrewBeacon

We have a successful company and website currently but it is a little dated. We have re-branded the company from Harbor Signal Networks to CrewBeacon and have a new logo for the new name. We are looking to build a newer fresher website with the new name. I will need a concept of the home page and one inside page. You can see our current site at https://www.harborsignalnetworks.example and the new site will be https://www.crewbeacon.example .

I also really like the https://www.pathlantern.example/ website. I like ledgerkite.example website. I like the https://skillorbit.example/ website.

See the attached document for layout and some text to use. Use the pictures I attached as opposed to pictures from the old site as much as you can.

Target Market(s)

Business

Industry/Entity Type

Software Service

Number of Pages Required

2 page

Font styles to use
Sans Serif

Requirements
Must have
• Use the colors from my logo. Professional but modern. We want people to feel like our product makes their staff feel safer at work.
Should not have
• Don't use any red or orange (no stop colors).

```html
<!DOCTYPE html>
<html lang="en">
<head>
<meta charset="utf-8">
<title>CrewBeacon — Home</title>
<link href="https://fonts.googleapis.com/css2?family=Montserrat:wght@400;500;600;700;800&family=Raleway:wght@400;500&display=swap" rel="stylesheet">
<style>
:root{
  --green:#5bab3c;
  --green-dark:#4a9a2e;
  --blue:#2f7fcb;
  --blue-dark:#2569b0;
  --ink:#222;
  --body:#444;
  --muted:#666;
  --footer-bg:#f3f3f3;
  --white:#fff;
}
*{margin:0;padding:0;box-sizing:border-box}
html,body{width:1200px;height:4071px;overflow:hidden;background:var(--white)}
body{position:relative;font-family:"Montserrat",sans-serif;color:var(--ink)}
.abs{position:absolute}
.btn{position:absolute;display:flex;align-items:center;justify-content:center;border-radius:24px;color:var(--white);font-weight:700;font-size:15px;text-decoration:none;letter-spacing:.2px}
.btn-blue{background:var(--blue)}
.btn-green{background:var(--green)}
.photo{position:absolute}

/* hero */
.hero{position:absolute;left:0;top:0;width:1200px;height:830px;background:linear-gradient(120deg,#4a4c4a 0%,#3a3c3b 45%,#2c2d2d 70%,#4d4f4c 100%)}
.hero-shade{position:absolute;inset:0;background:linear-gradient(90deg,rgba(0,0,0,.35),rgba(0,0,0,.05))}
.brand{position:absolute;display:flex;align-items:center;gap:12px;font-weight:600;font-size:36px;letter-spacing:-.5px}
.brand-dot{width:52px;height:52px;border-radius:50%}
.brand-hero{left:142px;top:55px;color:var(--white)}
.brand-hero .brand-dot{background:var(--white)}
.nav{position:absolute;top:72px;left:572px;display:flex;gap:24px;font-size:14px;font-weight:600}
.nav a{color:var(--white);text-decoration:none}
.nav a.active{color:var(--green)}
.hero-title{position:absolute;left:142px;top:262px;color:var(--white);font-weight:800;font-size:49px;line-height:57px;text-transform:uppercase}
.hero-sub{position:absolute;left:142px;top:442px;color:var(--white);font-family:"Raleway",sans-serif;font-size:20px}
.slider-arrow{position:absolute;top:676px}
.slider-dots{position:absolute;left:533px;top:687px;display:flex;gap:12px}
.slider-dots span{width:37px;height:3px;background:var(--white)}

/* features */
.feature{position:absolute;top:826px;display:flex;align-items:center;gap:22px}
.feature p{font-family:"Raleway",sans-serif;font-size:14px;line-height:19px;color:var(--body)}
.rule{position:absolute;left:142px;top:933px;width:914px;height:1px;background:#ddd}

/* product */
.product-img{left:150px;top:964px;width:270px;height:300px;border-radius:30px;background:radial-gradient(ellipse at 55% 55%,#3a2e28 0%,#2a2522 40%,rgba(255,255,255,0) 72%)}
.vline{position:absolute;left:470px;top:980px;width:1px;height:261px;background:#ddd}
.product-title{position:absolute;left:514px;top:991px;font-size:31px;line-height:43px;font-weight:800;text-transform:uppercase}
.product-text{position:absolute;left:514px;font-family:"Raleway",sans-serif;font-size:19px;color:var(--ink)}

/* why */
.why-bg{position:absolute;left:0;top:1304px;width:1200px;height:696px}
.section-title{position:absolute;left:0;width:1200px;text-align:center;font-weight:700;font-size:31px}
.underline{position:absolute;left:566px;width:70px;height:3px}
.card{position:absolute;background:var(--white);top:1543px;width:283px;height:296px;text-align:center;box-shadow:0 2px 8px rgba(0,0,0,.15)}
.card h3{position:absolute;left:0;width:100%;font-size:16px;font-weight:700;line-height:24px;text-transform:uppercase}
.card p{position:absolute;left:30px;width:223px;font-family:"Raleway",sans-serif;font-size:13.5px;line-height:21px;color:var(--body)}
.shield{position:absolute;top:1505px;width:124px;height:146px}
.options{position:absolute;left:57px;top:208px;display:grid;grid-template-columns:112px 90px;text-align:left;font-family:"Raleway",sans-serif;font-size:12px;line-height:18px;color:var(--ink)}

/* split panels */
.panel{position:absolute;top:2005px;height:403px}
.panel-text{position:absolute;color:var(--white);font-weight:700;font-size:28px;line-height:34px;text-align:center}
.stat{position:absolute;top:2255px;color:var(--white);font-family:"Raleway",sans-serif;font-size:16px}
.pill{position:absolute;left:846px;top:2247px;width:112px;height:38px;border:1.5px solid var(--white);border-radius:20px;display:flex;align-items:center;justify-content:center;color:var(--white);font-family:"Raleway",sans-serif;font-size:16px}

/* plan */
.plan{position:absolute;top:2593px;width:283px;height:327px;box-shadow:0 2px 8px rgba(0,0,0,.15);color:var(--white)}
.plan-img{position:absolute;left:0;top:0;width:283px;height:144px}
.plan h3{position:absolute;left:0;top:172px;width:100%;text-align:center;font-size:17px;line-height:24px;font-weight:700}
.plan ul{position:absolute;top:210px;list-style:none;font-family:"Raleway",sans-serif;font-size:14px;line-height:21px}
.plan ul li{display:flex;align-items:center;gap:10px}
.plan ul li::before{content:"";width:9px;height:9px;border-radius:50%;background:var(--white)}
.plan p{position:absolute;left:26px;top:232px;width:231px;text-align:center;font-family:"Raleway",sans-serif;font-size:13px;line-height:21px}

/* cta */
.cta-title{position:absolute;left:0;top:3202px;width:1200px;text-align:center;color:var(--white);font-weight:700;font-size:31px;line-height:44px}

/* footer */
.footer{position:absolute;left:0;top:3494px;width:1200px;height:419px;background:var(--footer-bg)}
.f-head{position:absolute;top:3560px;font-size:18px;font-weight:700;color:var(--ink)}
.f-phone{position:absolute;left:142px;top:3587px;font-size:22px;font-weight:800;letter-spacing:.5px}
.f-about{position:absolute;left:142px;top:3627px;width:290px;font-family:"Raleway",sans-serif;font-size:14.5px;line-height:22px;color:var(--body)}
.brand-foot{left:145px;top:3756px;color:var(--blue)}
.brand-foot .brand-dot{background:var(--blue)}
.f-links{position:absolute;top:3610px;list-style:none;font-family:"Raleway",sans-serif;font-size:15px;line-height:27.5px;color:var(--body)}
.social{position:absolute;top:3955px;width:32px;height:32px;border-radius:50%;border:2px solid var(--blue)}
.copyright{position:absolute;left:0;top:4008px;width:1200px;text-align:center;font-family:"Raleway",sans-serif;font-size:14px;color:var(--body)}
</style>
</head>
<body>

<!-- HERO -->
<section class="hero" role="img" aria-label="Office desk photo with a desk phone and a small panic button">
  <div class="hero-shade"></div>
</section>
<svg class="abs" style="left:0;top:720px" width="1200" height="112" viewBox="0 0 1200 112" aria-hidden="true">
  <polygon points="0,102 585,10 1200,102 1200,112 0,112" fill="#fff"/>
  <polygon points="0,88 585,0 585,10 0,102" fill="#5bab3c"/>
  <polygon points="585,0 1200,88 1200,96 585,10" fill="#2f7fcb"/>
</svg>

<div class="brand brand-hero"><span class="brand-dot"></span>CrewBeacon</div>
<nav class="nav">
  <a class="active" href="#">HOME</a>
  <a href="#">BUY ADDONS</a>
  <a href="#">CUST LOGIN</a>
</nav>
<a class="btn btn-green" href="#" style="left:898px;top:63px;width:158px;height:38px;font-size:13px">GET STARTED</a>

<h1 class="hero-title">Feel confident<br>that your staff<br>is protected</h1>
<p class="hero-sub">Get a revolutionary new electronic panic button</p>
<a class="btn btn-blue" href="#" style="left:142px;top:495px;width:187px;height:47px">GET STARTED</a>

<svg class="slider-arrow" style="left:60px" width="34" height="24" viewBox="0 0 34 24" aria-hidden="true"><path d="M32 12H3M13 2 3 12l10 10" fill="none" stroke="#fff" stroke-width="2.5"/></svg>
<svg class="slider-arrow" style="left:1106px" width="34" height="24" viewBox="0 0 34 24" aria-hidden="true"><path d="M2 12h29M21 2l10 10-10 10" fill="none" stroke="#fff" stroke-width="2.5"/></svg>
<div class="slider-dots"><span></span><span></span><span></span></div>

<!-- FEATURES -->
<div class="feature" style="left:142px">
  <svg width="60" height="72" viewBox="0 0 60 72" aria-hidden="true"><path d="M30 3 56 14v22c0 16-12 27-26 33C16 63 4 52 4 36V14Z" fill="none" stroke="#2f7fcb" stroke-width="3"/><circle cx="30" cy="36" r="6" fill="#5bab3c"/><circle cx="18" cy="40" r="5" fill="#2f7fcb"/><circle cx="42" cy="40" r="5" fill="#2f7fcb"/></svg>
  <p>Problems Stopped Before<br>They Start For Any Type Of<br>Organization</p>
</div>
<div class="feature" style="left:443px">
  <svg width="88" height="72" viewBox="0 0 88 72" aria-hidden="true"><circle cx="44" cy="36" r="26" fill="none" stroke="#2f7fcb" stroke-width="3"/><path d="M6 36h10M72 36h10" stroke="#5bab3c" stroke-width="3"/><text x="44" y="46" text-anchor="middle" font-family="Montserrat,sans-serif" font-size="28" font-weight="700" fill="#5bab3c">$</text></svg>
  <p>Affordable Prices Starting at<br>$18 per month. No Contracts.<br>No Hidden Costs</p>
</div>
<div class="feature" style="left:797px">
  <svg width="64" height="72" viewBox="0 0 64 72" aria-hidden="true"><rect x="6" y="28" width="52" height="36" fill="none" stroke="#2f7fcb" stroke-width="3"/><path d="M6 28l26 20 26-20" fill="none" stroke="#2f7fcb" stroke-width="3"/><rect x="16" y="6" width="32" height="28" fill="#fff" stroke="#5bab3c" stroke-width="3"/><path d="M22 14h20M22 21h20" stroke="#5bab3c" stroke-width="2.5"/></svg>
  <p>Alerts by computer,<br>mobile device, text, phone,<br>email, monitoring and E911</p>
</div>
<div class="rule"></div>

<!-- PRODUCT -->
<div class="photo product-img" role="img" aria-label="Photo of the dark panic button box with two push buttons and a cable"></div>
<div class="vline"></div>
<h2 class="product-title">Your empoyees shouldn’t feel<br>alone when they need help</h2>
<p class="product-text" style="top:1094px">Does this problem make you feel frustrated and anxious?</p>
<p class="product-text" style="top:1129px">Put a simple solution in their hands</p>
<a class="btn btn-blue" href="#" style="left:514px;top:1178px;width:186px;height:45px">GET STARTED</a>

<!-- WHY -->
<div class="why-bg" role="img" aria-label="Office photo with a green tint" style="background:linear-gradient(160deg,#6db544 0%,#5aa53a 50%,#4e9a33 100%)"></div>
<svg class="abs" style="left:0;top:1300px" width="1200" height="100" viewBox="0 0 1200 100" aria-hidden="true">
  <polygon points="0,0 585,0 0,92" fill="#fff"/>
  <polygon points="585,0 1200,0 1200,92" fill="#fff"/>
  <polygon points="585,4 1200,88 1200,98 585,12" fill="#2f7fcb"/>
</svg>
<h2 class="section-title" style="top:1414px;color:#fff">WHY BUSINESSES CHOOSE US?</h2>
<div class="underline" style="top:1471px;background:#fff"></div>

<div class="card" style="left:144px">
  <h3 style="top:128px">Easy to use</h3>
  <p style="top:166px">Press a button and let the right people know you need help and open a chat window letting everyone talk on resolving their problem.</p>
</div>
<div class="card" style="left:458px">
  <h3 style="top:118px">Communicate<br>the way you want</h3>
  <p style="top:172px">We give you lots of options:</p>
  <div class="options"><span>Computer</span><span>Text</span><span>Mobile</span><span>E911</span><span>Email</span><span>Call Center</span><span>Phone call</span></div>
</div>
<div class="card" style="left:773px">
  <h3 style="top:118px">Cost effective<br>protection</h3>
  <p style="top:180px">By leveraging your existing network and equipment we can lower your costs to give better options to your staff.</p>
</div>

<svg class="shield" style="left:224px" viewBox="0 0 124 146" aria-hidden="true"><path d="M62 2 120 34v38c0 34-26 60-58 72C30 132 4 106 4 72V34Z" fill="#2f7fcb" stroke="#fff" stroke-width="3"/><rect x="40" y="40" width="44" height="44" fill="none" stroke="#fff" stroke-width="3"/><circle cx="62" cy="62" r="9" fill="none" stroke="#fff" stroke-width="3"/></svg>
<svg class="shield" style="left:538px" viewBox="0 0 124 146" aria-hidden="true"><path d="M62 2 120 34v38c0 34-26 60-58 72C30 132 4 106 4 72V34Z" fill="#2f7fcb" stroke="#fff" stroke-width="3"/><path d="M62 38c15 0 26 10 26 22s-11 22-26 22c-4 0-8-1-11-2l-12 6 3-11c-4-4-6-9-6-15 0-12 11-22 26-22Z" fill="none" stroke="#fff" stroke-width="3"/><path d="M50 56h24M50 65h18" stroke="#fff" stroke-width="3"/></svg>
<svg class="shield" style="left:853px" viewBox="0 0 124 146" aria-hidden="true"><path d="M62 2 120 34v38c0 34-26 60-58 72C30 132 4 106 4 72V34Z" fill="#2f7fcb" stroke="#fff" stroke-width="3"/><text x="62" y="84" text-anchor="middle" font-family="Montserrat,sans-serif" font-size="52" font-weight="600" fill="#fff">$</text><path d="M32 90h20M72 90h20" stroke="#fff" stroke-width="3"/></svg>

<a class="btn btn-blue" href="#" style="left:506px;top:1886px;width:186px;height:46px">GET STARTED</a>

<!-- SPLIT PANELS -->
<div class="panel" role="img" aria-label="Dark photo of a desk phone and panic button" style="left:0;width:593px;background:linear-gradient(135deg,#3c3f40,#2a2c2e 60%,#3a3b3c)"></div>
<div class="panel" role="img" aria-label="Dark photo of a panic button mounted under a desk" style="left:602px;width:598px;background:linear-gradient(135deg,#2f3032,#43464a 50%,#2b2c2e)"></div>
<p class="panel-text" style="left:60px;top:2130px;width:440px">We know how scary it can<br>feel to worry about<br>employee safety.</p>
<a class="btn btn-blue" href="#" style="left:185px;top:2253px;width:185px;height:43px">START MY DEMO</a>
<p class="panel-text" style="left:652px;top:2122px;width:500px">That’s why we have provided<br>a way for customers to get help<br>to staff effectively in</p>
<span class="stat" style="left:745px">45 States</span>
<span class="pill">covering</span>
<span class="stat" style="left:972px">5 Countries</span>

<!-- SIMPLE START PLAN -->
<h2 class="section-title" style="top:2485px;color:var(--ink)">SIMPLE START PLAN</h2>
<div class="underline" style="top:2542px;background:var(--blue)"></div>

<div class="plan" style="left:144px;background:var(--green)">
  <div class="plan-img" role="img" aria-label="Photo of hands installing a button under a desk" style="background:linear-gradient(135deg,#6a6660,#a9a59c 60%,#5a5752)"></div>
  <h3>Explore Your Choices</h3>
  <ul style="left:100px;top:208px"><li>Pricing</li><li>Trial</li><li>Quote</li><li>Hardware</li></ul>
</div>
<div class="plan" style="left:458px;background:var(--blue)">
  <div class="plan-img" role="img" aria-label="Photo of a hand pressing a wall mounted button" style="background:linear-gradient(135deg,#5a5f62,#9aa1a6 55%,#3e4245)"></div>
  <h3>Get Setup</h3>
  <ul style="left:66px;top:208px"><li>Input Your Alerts</li><li>Input Your Staff</li><li>Install Our Software</li></ul>
</div>
<div class="plan" style="left:773px;background:var(--green)">
  <div class="plan-img" role="img" aria-label="Photo of a hand holding a small alert fob by a pocket" style="background:linear-gradient(135deg,#c9cdd2,#5b6b82 55%,#2f3a4d)"></div>
  <h3 style="top:160px">Feel Confident<br>Your Staff Is Protected</h3>
  <p>High Five. You just too a major step to getting rid of the anxiety and frustration this gave you.</p>
</div>

<a class="btn btn-blue" href="#" style="left:495px;top:2977px;width:210px;height:44px">START MY DEMO</a>

<!-- CTA -->
<div class="abs" role="img" aria-label="Desk phone photo with a blue to green tint" style="left:0;top:3107px;width:1200px;height:387px;background:linear-gradient(100deg,#2f7fcb 0%,#3b8fa8 40%,#4fa263 70%,#5bab3c 100%)"></div>
<svg class="abs" style="left:0;top:3104px" width="1200" height="100" viewBox="0 0 1200 100" aria-hidden="true">
  <polygon points="0,0 585,0 0,98" fill="#fff"/>
  <polygon points="585,0 1200,0 1200,62" fill="#fff"/>
  <polygon points="0,92 585,3 585,12 0,100" fill="#5bab3c"/>
</svg>
<h2 class="cta-title">Stay Connected with<br>Staff during a Crisis Situations</h2>
<a class="btn btn-blue" href="#" style="left:507px;top:3320px;width:211px;height:44px">START MY DEMO</a>

<!-- FOOTER -->
<footer class="footer"></footer>
<h4 class="f-head" style="left:142px">CALL US</h4>
<p class="f-phone">1 – 800 – 555 – 0142</p>
<p class="f-about">When employees feel alone during a threatening situation, we give them a way to let the right resources know that they need help so you can feel confident that your staff is protected.</p>
<div class="brand brand-foot"><span class="brand-dot"></span>CrewBeacon</div>

<h4 class="f-head" style="left:539px">SHOP</h4>
<ul class="f-links" style="left:539px"><li>Add Ons</li><li>Start My Demo</li><li>Custom Quote</li><li>Start Trial</li></ul>
<h4 class="f-head" style="left:727px">ABOUT</h4>
<ul class="f-links" style="left:727px"><li>Affiliates</li><li>Contact</li><li>Support</li><li>Existing Customers</li><li>Industries</li><li>Blog</li><li>FAQ</li></ul>
<h4 class="f-head" style="left:918px">LEGAL</h4>
<ul class="f-links" style="left:918px"><li>Privacy Policy</li><li>Terms of Use</li><li>End User License</li><li>Agreement</li></ul>

<span class="social" style="left:520px" aria-label="Social link"></span>
<span class="social" style="left:563px" aria-label="Social link"></span>
<span class="social" style="left:605px" aria-label="Social link"></span>
<span class="social" style="left:648px" aria-label="Social link"></span>
<p class="copyright">CrewBeacon © 2020 All Rights Reserved | Privacy Policy | Terms and Conditions</p>

</body>
</html>
```